LIFE CHANGING NEW WEBSITE DESIGN NEEDED FOR FULL WEBSITE- FUN/FEMININE!

I need a website designed for a personal financial advice website geared at women called LADY COIN MAVEN. I will be providing free financial advice around topics of making, saving, spending and sharing money. The concept is to change the way women understand money and the necessity around building various passive income streams to ensure full financial freedom. This will then carry down to advice for mothers with children and children in particular. The website should be elegant and yet witty. I don't want lots of serious photos but more relatable. I will have a photo of myself and my story as this is a blog and needs to be relatable to women and mothers. I like pinks and greys. I want to have a pink piggy bank being broken with a hammer in the front screen to break our traditional mindset around piggy bank saving/spending habits. I have created a logo that is a pink piggy head with LADY COIN MAVEN that needs to be incorporated so that it blends into the heading. I have also already started designing the website on Squarespace and can provide access to that. Basically it should have a format of LADY COIN MAVEN LOGO center in header then on left hand navigation: MAKE, SAVE, SPEND, SHARE then on right hand header navigation: MISSION, GET STARTED, CONTACT LCM I would like to have the front page when you go to the url to have the image of the piggy bank being broken then a catchy phrase then under 4 boxes with MAKE (image and description) SAVE (image and description) SPEND (image and description) SHARE (image and description) if you click on those or the title they go to pages that are dedicated to each them. Each page should have a little intro on the topic then I want lots of blog links as I will be mainly writing blogs. Each blog site should have ability to write comments as well. I need social media icons on each page too. Please let me know what you need from me to get started. I prefer having a discussion if possible to not waste anyone's time. I need the site to be easy for me to use and add blogs/urls etc as needed. I also need the site to be put into my domain that I already purchased: www.ladycoinmaven.example

Target Market(s)

teenage girls, 20 something girls, 30 something girls and mothers

Coding

Coded - Design and coding required

Number of Pages Required

5+ page

Font styles to use
Sans Serif

Colors
e667a6
e34197
f59195
eea4c8
aaaaaa
cbcbcb
959595

Requirements
Must have
• TOP NAVIGATION
• MAKE SAVE SPEND SHARE LOGO/LADY COIN MAVEN MISSION GET STARTED CONTACT LCM
• FRONT PAGE: IMAGE OF PIGGY BANK BEING BROKEN WITH A HAMMER
• CATCH PHRASE OVER THE IMAGE
• BUTTON IN PINK- TAKE ACTION (WHICH DIRECTS TO TAKE ACTION TAB ON NAVIGATION HEADER
• 4 BOXES BELOW MAIN IMAGE WITH IMAGE/DESCRIPTIONS FOR MAKE, SAVE, SPEND, SHARE THAT EACH GO TO THE PAGES FROM THE NAVIGATION HEADER
• EACH PAGE SHOULD BE DEDICATED TO THOSE TOPICS THEN THERE IS AN INTRO ON EACH PAGE THEN THE LINKS TO DIFFERENT BLOGS AROUND EACH TOPIC FOR MAKE, SAVE, SPEND, SHARE
• EACH BLOG SHOULD HAVE COMMENTS SECTION AND SOCIAL MEDIA ICONS
• (GOOD TO USE PINKS/GREYS)
Should not have
• BE SUPER BUSY, CLUTTERED, FEEL LIKE I AM SELLING SOMETHING

```html
<!DOCTYPE html>
<html lang="en">
<head>
<meta charset="utf-8">
<title>Lady Coin Maven — Testimonials</title>
<link href="https://fonts.googleapis.com/css2?family=Rokkitt:wght@400&family=Noticia+Text:ital@1&family=Open+Sans:wght@600&display=swap" rel="stylesheet">
<style>
:root{
  --admin-bg:#23282d;
  --pink-line:#e667a6;
  --pink-name:#c8457f;
  --pink-brand:#e34197;
  --nav-text:#959595;
  --band:#f3f3f3;
  --ink:#333333;
  --body-text:#555555;
  --star:#cbcbcb;
  --footer:#4a4a4a;
  --social:#d4b596;
  --link-tan:#e0bc98;
}
*{margin:0;padding:0;box-sizing:border-box}
html,body{width:1200px;height:595px;overflow:hidden;background:var(--band)}
body{position:relative;font-family:"Rokkitt",serif}
.admin-bar{position:absolute;left:0;top:0;width:1200px;height:17px;background:var(--admin-bg);border-bottom:2px solid var(--pink-line);display:flex;align-items:center;padding:0 8px;font-family:"Open Sans",sans-serif;font-weight:600;font-size:6.2px;color:#eee;gap:9px}
.admin-bar .dot{width:7px;height:7px;border-radius:50%;border:1px solid #aaa}
.admin-bar .right{margin-left:auto;display:flex;gap:6px;align-items:center}
.admin-bar .avatar{width:7px;height:7px;background:#cbcbcb}
.site-header{position:absolute;left:0;top:17px;width:1200px;height:46px;background:#fff;box-shadow:0 1px 2px rgba(0,0,0,.05)}
.main-nav{position:absolute;top:17px;left:418px;display:flex;gap:23px;font-size:11px;color:var(--nav-text);white-space:nowrap;line-height:1}
.testimonials{position:absolute;left:0;top:116px;width:1200px;height:379px}
.faces{position:absolute;inset:0;background:linear-gradient(100deg,#8e7a70 0%,#b49c8e 20%,#a89590 40%,#9c8a80 60%,#b7a293 80%,#8f7c74 100%)}
.quote-mark{position:absolute;left:577px;top:44px}
.card{position:absolute;left:267px;top:102px;width:665px;height:201px;background:#fff}
.slide{position:absolute;top:0;width:200px;height:201px;text-align:center}
.slide > *{position:absolute;left:0;width:200px}
.slide .avatar{left:80px;width:39px;height:39px;top:25px;border-radius:50%;background:linear-gradient(160deg,#b7835e,#e8cfb8)}
.slide h3{top:74px;font-family:"Noticia Text",serif;font-style:italic;font-weight:400;font-size:12px;line-height:18px;color:var(--ink);white-space:nowrap}
.slide .stars{top:97px;display:flex;justify-content:center}
.slide p{top:115px;left:12px;width:176px;font-size:7.7px;line-height:12.4px;color:var(--body-text)}
.slide .name{top:167px;font-family:"Noticia Text",serif;font-style:italic;font-size:7.8px;line-height:12px;color:var(--pink-name)}
.bullets{position:absolute;left:591px;top:328px;display:flex;gap:3px}
.bullets span{width:4px;height:4px;border-radius:50%;background:#cbcbcb}
.bullets span.on{background:var(--pink-line)}
.site-footer{position:absolute;left:0;top:507px;width:1200px;height:88px;background:var(--footer)}
.brand{position:absolute;left:260px;top:33px;width:80px;text-align:center;color:var(--pink-brand);font-family:"Rokkitt",serif;font-size:7px;line-height:1}
.brand .mark{display:block;width:10px;height:10px;border-radius:50%;border:1px solid var(--pink-brand);margin:0 auto 3px}
.social{position:absolute;left:564px;top:27px;display:flex;gap:1px}
.social span{width:24px;height:23px;background:var(--social);display:flex;align-items:center;justify-content:center}
.social span i{width:5px;height:5px;border-radius:50%;background:#fff}
.copyright{position:absolute;left:820px;top:33px;font-family:"Open Sans",sans-serif;font-weight:600;font-size:7.5px;color:#fff}
.copyright a{color:var(--link-tan);font-family:"Rokkitt",serif;font-weight:400;font-size:8.5px}
.to-top{position:absolute;left:1162px;top:31px;width:26px;height:26px;border-radius:50%;background:#fff;display:flex;align-items:center;justify-content:center}
</style>
</head>
<body>
<svg width="0" height="0" style="position:absolute"><defs><path id="star" d="M4 0l1 2.7h3l-2.4 1.8 1 2.9L4 5.6 1.4 7.4l1-2.9L0 2.7h3z"/></defs></svg>
<div class="admin-bar">
  <span class="dot"></span><span>Lady Coin Maven</span><span>Customize</span><span>↻ 6</span><span>0</span><span>+ New</span><span>Edit Page</span><span>Slide Forge</span>
  <div class="right"><span>Howdy, admin</span><span class="avatar"></span></div>
</div>

<header class="site-header">
  <nav class="main-nav"><span>Make</span><span>Save</span><span>Spend</span><span>Share</span><span>Mission</span><span>Get Started</span><span>Contact Me</span></nav>
</header>

<section class="testimonials">
  <div class="faces" role="img" aria-label="Mosaic background of smiling portrait photos of many different women and men"></div>
  <svg class="quote-mark" width="47" height="38" viewBox="0 0 47 38" aria-hidden="true">
    <path fill="#fff" d="M2 2h16v16c0 10-5 17-15 20l-2-4c5-2 8-6 8-10H2z M27 2h16v16c0 10-5 17-15 20l-2-4c5-2 8-6 8-10h-7z"/>
  </svg>
  <div class="card">
    <div class="slide" style="left:22px">
      <div class="avatar" role="img" aria-label="Portrait of Nora Pell"></div>
      <h3>New outlook on life</h3>
      <div class="stars"><svg width="42" height="8" viewBox="0 0 42 8"><g fill="var(--star)"><use href="#star"/><use href="#star" x="8.5"/><use href="#star" x="17"/><use href="#star" x="25.5"/><use href="#star" x="34"/></g></svg></div>
      <p>Nullam vel malesuada nisi. Vestibulum ante ipsum primis in faucibus orci luctus et ultrices posuere cubilia curae</p>
      <div class="name">Nora Pell</div>
    </div>
    <div class="slide" style="left:232px">
      <div class="avatar" role="img" aria-label="Portrait of Elsie Varn" style="background:linear-gradient(160deg,#c9a36e,#f0ddc8)"></div>
      <h3>She’s just amazing</h3>
      <div class="stars"><svg width="42" height="8" viewBox="0 0 42 8"><g fill="var(--star)"><use href="#star"/><use href="#star" x="8.5"/><use href="#star" x="17"/><use href="#star" x="25.5"/><use href="#star" x="34"/></g></svg></div>
      <p>Aenean est nisl, ultricies a efficitur in, posuere quis nibh. Integer mollis ex magna, in efficitur sapien inter</p>
      <div class="name">Elsie Varn</div>
    </div>
    <div class="slide" style="left:443px">
      <div class="avatar" role="img" aria-label="Portrait of Nora Pell"></div>
      <h3>New outlook on life</h3>
      <div class="stars"><svg width="42" height="8" viewBox="0 0 42 8"><g fill="var(--star)"><use href="#star"/><use href="#star" x="8.5"/><use href="#star" x="17"/><use href="#star" x="25.5"/><use href="#star" x="34"/></g></svg></div>
      <p>Nullam vel malesuada nisi. Vestibulum ante ipsum primis in faucibus orci luctus et ultrices posuere cubilia curae</p>
      <div class="name">Nora Pell</div>
    </div>
  </div>
  <div class="bullets"><span class="on"></span><span></span></div>
</section>

<footer class="site-footer">
  <div class="brand"><span class="mark"></span>Lady Coin Maven</div>
  <div class="social" aria-label="Social links"><span><i></i></span><span><i></i></span><span><i></i></span></div>
  <div class="copyright">© Copyright <a href="#">Lady Coin Maven</a></div>
  <div class="to-top"><svg width="10" height="10" viewBox="0 0 10 10" aria-hidden="true"><path fill="#959595" d="M5 0l5 5H7v5H3V5H0z"/></svg></div>
</footer>
</body>
</html>
```